Zielgruppe
Massage-Velora macht Rücken/ Ganzkörpermassage, Intim/ Körperrasur, verschiedene Wellnessanwendungen ...
Ich suche einen neutralen modernen Flyer für Hotels/ Restaurants/ Designshops wie Tolv/ Mendra ...
Leider ist mein Grafiker Anfang Mai nach Krankheit plötzlich verstorben!
Anbei viele Motive .. vielleicht finde ich hier wieder einen Partner für Anzeigen/ Aufkleber und Flyer!
Herzlichen Dank
Wilfried
Aufgabenstellung
Postkartenformat
Dopp Visitenkarte

```html
<!DOCTYPE html>
<html lang="de">
<head>
<meta charset="utf-8">
<title>Massage-Velora Flyer A6</title>
<link href="https://fonts.googleapis.com/css2?family=Fira+Sans:wght@600;700&family=Open+Sans:wght@300;400&display=swap" rel="stylesheet">
<style>
  :root {
    --orange: #ee7f0e;
    --orange-dark: #c85a19;
    --orange-soft: #f7b26b;
    --blue: #0a9ddf;
    --ink: #4d4d4d;
    --paper: #ffffff;
    --stage: #3b2a20;
  }
  * { margin: 0; padding: 0; box-sizing: border-box; }
  html, body { width: 1200px; height: 849px; overflow: hidden; background: var(--stage); }
  .stage { position: relative; width: 1200px; height: 849px; }
  .flyer {
    position: absolute; top: 77px; width: 493px; height: 695px;
    background: var(--paper); overflow: hidden;
    font-family: "Open Sans", sans-serif;
  }
  .flyer--left { left: 80px; }
  .flyer--right { left: 627px; }

  .photo { position: absolute; left: 0; right: 0; }
  .flyer--left .photo {
    top: 215px; height: 380px;
    background: linear-gradient(to bottom, rgba(255,255,255,1) 0%, #f6dcc8 25%, #ecbf9c 60%, #dfa37b 100%);
  }
  .flyer--right .photo {
    top: 250px; height: 340px;
    background: linear-gradient(to bottom, rgba(255,255,255,1) 0%, #f7e6da 25%, #efd1bc 60%, #e6bd9f 100%);
  }

  .title {
    position: absolute; left: 22px; top: 30px;
    font-family: "Fira Sans", sans-serif; font-weight: 700;
    color: var(--orange); font-size: 56px; line-height: 50px; letter-spacing: 0.5px;
  }
  .phone {
    position: absolute; left: 23px; top: 131px;
    font-family: "Fira Sans", sans-serif; font-weight: 700;
    color: var(--orange-dark); font-size: 25px;
  }
  .badge-service {
    position: absolute; left: 346px; top: 0; width: 116px; height: 116px;
    border-radius: 50%; background: var(--blue); color: #fff;
    display: flex; flex-direction: column; align-items: center; justify-content: center;
    font-family: "Fira Sans", sans-serif; font-weight: 600; font-size: 14px; line-height: 14px;
    transform: rotate(-4deg); padding-top: 4px;
  }

  .services { position: absolute; left: 24px; color: var(--ink); font-size: 19.5px; line-height: 25px; }
  .flyer--left .services { top: 188px; }
  .services .dot { color: var(--orange); }

  .service-list { position: absolute; left: 38px; color: var(--ink); font-size: 18.5px; line-height: 25px; }
  .service-list--de { top: 196px; }
  .service-list--en { top: 356px; }
  .tag-new {
    display: inline-block; width: 21px; height: 21px; border-radius: 50%;
    background: var(--blue); color: #fff; border: 1.5px solid #fff;
    font-family: "Fira Sans", sans-serif; font-weight: 600; font-size: 7px;
    line-height: 18px; text-align: center; vertical-align: 4px; margin-left: 6px;
  }

  .band { position: absolute; left: 0; top: 0; width: 493px; height: 695px; }

  .seal {
    position: absolute; left: 297px; top: 466px; width: 172px; height: 172px;
    border-radius: 50%; background: var(--orange); border: 7px solid #fff;
    color: #fff; font-family: "Fira Sans", sans-serif; text-align: center;
    display: flex; flex-direction: column; justify-content: center;
  }
  .seal__top { font-weight: 700; font-size: 30px; line-height: 34px; }
  .seal__main { font-weight: 700; font-size: 34px; line-height: 38px; }
  .seal__sub { font-weight: 400; font-family: "Open Sans", sans-serif; font-size: 20px; line-height: 26px; }

  .contact {
    position: absolute; left: 26px; top: 600px; max-width: 266px;
    color: #fff; font-size: 14px; font-weight: 300; line-height: 20px; white-space: nowrap;
  }
  .contact .dot { color: var(--orange-soft); }
  .web {
    position: absolute; left: 24px; top: 650px; color: #fff;
    font-family: "Fira Sans", sans-serif; font-weight: 700; font-size: 18px;
  }
  .appointment { position: absolute; right: 26px; top: 655px; color: var(--orange-soft); font-size: 15px; font-weight: 300; }
</style>
</head>
<body>
<main class="stage">

  <section class="flyer flyer--left">
    <div class="photo" role="img" aria-label="Foto: lächelnder Mann liegt entspannt auf einer Massageliege"></div>
    <h1 class="title">MASSAGE<br>VELORA</h1>
    <p class="phone">0175-480 39 12</p>
    <div class="badge-service"><span>Studio &amp; Outcall</span><span>Haus / Hotel</span></div>
    <p class="services">Ganzkörper <span class="dot">·</span> Rücken · Po-Relax <span class="dot">·</span> Intimrasur<br>Fußmassage <span class="dot">·</span> Bondagemassage</p>
    <svg class="band" viewBox="0 0 493 695" aria-hidden="true">
      <path d="M0 545 Q200 605 493 505 L493 695 L0 695 Z" fill="var(--orange-dark)"/>
      <path d="M0 551 Q200 611 493 511 L493 695 L0 695 Z" fill="#fff"/>
      <path d="M0 560 Q200 620 493 520 L493 695 L0 695 Z" fill="var(--orange)"/>
    </svg>
    <div class="seal"><span class="seal__top">KEIN</span><span class="seal__main">RUHETAG</span><span class="seal__sub">OPEN DAILY</span></div>
    <p class="contact">Studio Alm 12 <span class="dot">·</span> 4. OG <span class="dot">·</span> 80331 München<br>info@massage-velora.ch</p>
    <p class="web">MASSAGE-VELORA.COM</p>
    <p class="appointment">Termin nach Vereinbarung</p>
  </section>

  <section class="flyer flyer--right">
    <div class="photo" role="img" aria-label="Foto: Mann mit geschlossenen Augen genießt eine Nackenmassage"></div>
    <h1 class="title">MASSAGE<br>VELORA</h1>
    <p class="phone">0175-480 39 12</p>
    <div class="badge-service"><span>Studio &amp; Outcall</span><span>Haus / Hotel</span></div>
    <p class="service-list service-list--de">Rücken- &amp; Ganzkörpermassage<br>Po Relax Massage, Tantra<br>Bondage (Fessel) Massage<span class="tag-new">NEU</span><br>Streichen &amp; Berührung<br>Intim- &amp; Körperrasur</p>
    <p class="service-list service-list--en">full body massage, swedish<br>buttockmassage, tantric<br>bondage massage<span class="tag-new">NEW</span><br>gentle touch, foam massage<br>intimate- &amp; body shaving</p>
    <svg class="band" viewBox="0 0 493 695" aria-hidden="true">
      <path d="M0 545 Q200 605 493 505 L493 695 L0 695 Z" fill="var(--orange-dark)"/>
      <path d="M0 551 Q200 611 493 511 L493 695 L0 695 Z" fill="#fff"/>
      <path d="M0 560 Q200 620 493 520 L493 695 L0 695 Z" fill="var(--orange)"/>
    </svg>
    <div class="seal"><span class="seal__top">KEIN</span><span class="seal__main">RUHETAG</span><span class="seal__sub">OPEN DAILY</span></div>
    <p class="contact">Studio Alm 12 <span class="dot">·</span> 4. OG <span class="dot">·</span> 80331 München<br>info@massage-velora.ch</p>
    <p class="web">MASSAGE-VELORA.COM</p>
    <p class="appointment">Termin nach Vereinbarung</p>
  </section>

</main>
</body>
</html>
```